Criminal Defense law firm needs website and logo

Need a logo design and web design for a small firm in Miami, Florida. The firm concentrates in the areas of state and federal criminal defense in Miami Dade County, Florida.The firm handles cases in the areas of Drug Possession, Fraud Offenses, Traffic Offenses, domestic violence, Violent Crimes, probation violation, Juvenile Delinquency, and expunction/expungment of criminal records (detailed list provided in attachment). The name of the attorney is Loreta Benavides-Kurtz. Sole Practitioner. Will attach profile. (the attachment are from my previous law firm, can use any of the language but adjust to a sole practitioner)

Industry/Entity Type

Lawyer

Number of Pages Required

3 page

Font styles to use
Serif

Colors
0356a4

Requirements
Must have
• Page that includes area's of practice. Page for Attorney profile. Contact page indicating that we speak Spanish and accept all major credit cards.

```html
<!DOCTYPE html>
<html lang="en">
<head>
<meta charset="utf-8">
<title>Loreta Benavides-Kurtz — Attorney at Law</title>
<link rel="stylesheet" href="https://fonts.googleapis.com/css2?family=Roboto+Condensed:wght@400;700&family=Open+Sans:ital,wght@0,400;0,600;0,700;1,400&display=swap">
<style>
:root{
  --blue:#0356a4;
  --navy:#1c3557;
  --bronze:#a88660;
  --bronze-deep:#9c7a52;
  --ink:#333;
  --muted:#666;
  --panel:#e3e3e3;
  --footer:#1f2229;
  --white:#fff;
}
*{margin:0;padding:0;box-sizing:border-box}
html,body{width:682px;height:1200px;overflow:hidden;background:var(--white)}
body{position:relative;font-family:"Open Sans",sans-serif;color:var(--ink);font-size:6px}
.abs{position:absolute}
.cond{font-family:"Roboto Condensed",sans-serif}

.topbar{left:0;top:0;width:682px;height:15px;background:var(--bronze);color:var(--white);font-size:5.5px;display:flex;justify-content:flex-end;align-items:center;gap:12px;padding-right:125px}
.topbar span{display:flex;align-items:center;gap:3px}
.topbar b{font-weight:700}

.hero{left:0;top:15px;width:682px;height:235px;background:linear-gradient(180deg,#dde6ef 0%,#c9d7e6 45%,#a9bdd3 60%,#8ea4bd 100%)}
.skyline{left:0;top:125px;width:682px;height:110px;background:linear-gradient(180deg,rgba(120,140,165,.0) 0%,#7d8ea5 30%,#4c5a70 75%,#2c3446 100%)}
.brand{left:125px;top:26px;color:var(--blue);font-weight:700;font-size:8.5px;letter-spacing:.2px;line-height:1.2}
.brand small{display:block;font-size:4.5px;letter-spacing:1.5px;color:var(--muted);font-weight:600}
.nav{right:125px;top:36px;display:flex;gap:15px;font-size:5.8px;font-weight:700;color:#222}
.nav .on{color:var(--blue)}
.hero-title{left:0;width:682px;top:64px;text-align:center;color:var(--blue);font-weight:700;font-size:20.5px}
.hero-quote{left:135px;width:412px;top:93px;text-align:center;font-size:6.2px;line-height:9px;color:#222}
.qmark{font-family:Georgia,serif;font-size:22px;color:var(--white);font-weight:700}
.hero-author{left:0;width:682px;top:115px;text-align:center;font-size:6px;color:#222;font-weight:700}
.hero-author span{color:var(--muted);font-weight:400}

.section-title{font-family:"Roboto Condensed",sans-serif;font-weight:700;color:var(--navy);font-size:11px}
.rule{height:2px;background:#ddd}

.portrait{left:125px;top:276px;width:110px;height:118px;background:linear-gradient(160deg,#8a8a8a,#4a4a4a);box-shadow:3px 3px 0 #d5d5d5}
.about-text{left:261px;top:298px;width:296px;font-size:6.1px;line-height:9.8px;color:#555}
.btn{left:261px;top:376px;width:72px;height:15px;background:var(--bronze);color:var(--white);font-size:5.5px;font-weight:700;display:flex;align-items:center;justify-content:center;letter-spacing:.3px}

.practice{left:0;top:420px;width:682px;height:206px;background:var(--panel)}
.card{top:464px;width:134px;height:137px;background:var(--white);box-shadow:1px 1px 3px rgba(0,0,0,.25);padding:4px}
.card .ph{width:126px;height:68px}
.card h3{font-family:"Roboto Condensed",sans-serif;font-weight:700;color:var(--navy);font-size:7.5px;margin:8px 2px 3px}
.card p{font-size:5.7px;line-height:8px;color:#444;margin:0 2px}
.card a{display:block;margin:4px 2px 0;font-size:5.6px;font-weight:700;color:var(--blue);text-decoration:none}

.testimonial{left:140px;width:402px;top:696px;text-align:center;font-style:italic;font-size:6.2px;line-height:9.5px;color:#555}
.testimonial-name{left:0;width:682px;top:730px;text-align:center;font-size:5.6px;font-weight:700;color:#222}

.cases{left:0;top:758px;width:682px;height:136px;background:linear-gradient(180deg,#f1f1f1,#e6e6e6)}
.case{top:803px;width:100px}
.case .ph{height:57px}
.case p{margin-top:6px;font-family:"Roboto Condensed",sans-serif;font-size:7.2px;color:#222}

.contact{left:0;top:894px;width:682px;height:181px;background:linear-gradient(180deg,#a6845c,#93734d)}
.field{height:14px;border:1px solid rgba(255,255,255,.35);background:rgba(80,55,30,.25);color:#f1e6d8;font-size:5.2px;padding:3px 5px}
.submit{left:356px;top:1012px;width:72px;height:16px;background:var(--white);color:#222;font-size:5.6px;font-weight:700;display:flex;align-items:center;justify-content:center;letter-spacing:.4px}
.agree{left:250px;top:1016px;font-size:5.6px;color:#f1e6d8;font-style:italic;display:flex;align-items:center;gap:4px}
.agree b{font-style:normal;color:var(--white)}
.tick{width:6px;height:6px;background:var(--white)}
.note{left:152px;width:390px;top:1040px;font-size:5.5px;line-height:8.4px;color:#efe2d0}

.footer{left:0;top:1075px;width:682px;height:125px;background:var(--footer);color:#c4c7cc}
.footer h4{font-family:"Roboto Condensed",sans-serif;font-weight:400;color:var(--white);font-size:7px;letter-spacing:.3px}
.links{font-size:5.6px;line-height:12.4px;color:#a9adb4}
.links .on{color:var(--white)}
.fc-row{display:flex;gap:6px;align-items:flex-start;font-size:5.4px;line-height:7.5px;margin-bottom:6px}
.fc-row b{color:var(--white);font-size:6px}
.ic{width:10px;height:10px;flex:none}
.fbrand{left:430px;top:1105px;width:120px;text-align:center;color:#6b7078;font-size:8.5px;font-weight:700;line-height:1.3}
.fbrand small{display:block;font-size:4.5px;letter-spacing:1.5px;font-weight:600}
.social{left:448px;top:1146px;display:flex;gap:5px}
.social i{width:11px;height:11px;border-radius:50%;background:#3e6ea8;display:block}
.copy{left:400px;width:180px;top:1164px;text-align:center;font-size:5.2px;color:#8d9198}
.copy b{color:var(--white);font-weight:600}
</style>
</head>
<body>

<header class="abs topbar">
  <span><svg width="6" height="5" viewBox="0 0 6 5"><rect x=".3" y=".3" width="5.4" height="4.4" fill="none" stroke="#fff" stroke-width=".6"/><path d="M.3 .4 3 2.6 5.7 .4" fill="none" stroke="#fff" stroke-width=".6"/></svg>hello@benavideslaw.net</span>
  <span><svg width="5" height="6" viewBox="0 0 5 6"><path d="M1 0h1l.5 1.6-.8.6a3 3 0 0 0 1.4 1.6l.6-.7L5 3.6V5L4 6C1.8 5.6.2 3.6 0 1.2Z" fill="#fff"/></svg><b>305-555-0148</b></span>
  <span><svg width="6" height="5" viewBox="0 0 6 5"><path d="M3 0 6 2.5H5V5H3.7V3.3H2.3V5H1V2.5H0Z" fill="#fff"/></svg>1450 Brickell Bay Drive, Suite 900, Miami, FL 33131</span>
</header>

<section class="abs hero" role="img" aria-label="Downtown waterfront skyline at dusk under a pale blue sky"></section>
<div class="abs skyline" role="img" aria-label="City towers and harbour bridge"></div>

<div class="abs brand">Loreta Benavides-Kurtz<small>ATTORNEY AT LAW</small></div>
<nav class="abs nav"><span class="on">HOME</span><span>FIRM PROFILE</span><span>ATTORNEYS</span><span>CASE RESULTS</span><span>RESOURCES</span><span>BLOG</span><span>CONTACT</span></nav>

<h1 class="abs hero-title cond">FEDERAL AND STATE CRIMINAL DEFENSE</h1>
<span class="abs qmark" style="left:122px;top:84px">&ldquo;</span>
<p class="abs hero-quote">In the cause of freedom, we have to battle for the rights of the people with whom we do not agree; and whom, in many cases, we may not like. These people test the strength of the freedoms, which protect all of us. If we do not defend their rights, we endanger our own.</p>
<span class="abs qmark" style="left:517px;top:97px">&rdquo;</span>
<p class="abs hero-author">WALTER HALE <span>(Statesman)</span></p>

<div class="abs portrait" role="img" aria-label="Portrait photograph of the attorney"></div>
<h2 class="abs section-title" style="left:261px;top:278px">ABOUT OUR ATTORNEY</h2>
<div class="abs rule" style="left:370px;top:284px;width:187px"></div>
<p class="abs about-text">Lorem ipsum dolor sit amet, consectetur adipiscing elit. In vulputate vulputate rutrum. Praesent vulputate felis eget metus pharetra dictum. Ut venenatis pulvinar condimentum. Nam sed augue elit. Sed fringilla, sapien quis consequat tempor, leo velit dictum libero, id euismod dolor ligula ut felis. Donec leo enim, suscipit ac pharetra vel, varius ac nisl. Maecenas pulvinar, velit id vestibulum tristique, libero tellus elementum quam, non imperdiet massa est ut odio. Nam id enim pharetra, euismod enim nec, laoreet elit. Nulla luctus, odio sed venenatis condimentum, risus libero lobortis mi, ut volutpat nisi felis sit amet dui.</p>
<div class="abs btn">VIEW PROFILE</div>

<section class="abs practice"></section>
<h2 class="abs section-title" style="left:125px;top:440px">PRACTICE AREA</h2>
<div class="abs rule" style="left:200px;top:446px;width:357px;background:#cfcfcf"></div>
<svg class="abs" style="left:96px;top:527px" width="10" height="18" viewBox="0 0 10 18"><path d="M9 1 1 9l8 8" fill="none" stroke="#666" stroke-width="1.2"/></svg>
<svg class="abs" style="left:574px;top:527px" width="10" height="18" viewBox="0 0 10 18"><path d="m1 1 8 8-8 8" fill="none" stroke="#666" stroke-width="1.2"/></svg>

<article class="abs card" style="left:125px">
  <div class="ph" role="img" aria-label="Photo illustrating drug possession charges" style="background:linear-gradient(135deg,#8a8276,#3d3a36)"></div>
  <h3>DRUG POSSESSION</h3>
  <p>Lorem ipsum dolor sit amet, consectetur adipiscing elit. In vulputate vulputate rutrum. Praesent vulputate felis eget.</p>
  <a>Read More &raquo;</a>
</article>
<article class="abs card" style="left:273px">
  <div class="ph" role="img" aria-label="Photo of hands in handcuffs" style="background:linear-gradient(135deg,#5a5a5c,#1f1f22)"></div>
  <h3>DRUG POSSESSION</h3>
  <p>Lorem ipsum dolor sit amet, consectetur adipiscing elit. In vulputate vulputate rutrum. Praesent vulputate felis eget.</p>
  <a>Read More &raquo;</a>
</article>
<article class="abs card" style="left:421px">
  <div class="ph" role="img" aria-label="Photo of a driver stopped in a car" style="background:linear-gradient(135deg,#9fb1b8,#4a6470)"></div>
  <h3>TRAFFIC OFFENSES</h3>
  <p>Lorem ipsum dolor sit amet, consectetur adipiscing elit. In vulputate vulputate rutrum. Praesent vulputate felis eget.</p>
  <a>Read More &raquo;</a>
</article>

<div class="abs rule" style="left:125px;top:652px;width:160px;background:#e6e6e6"></div>
<h2 class="abs section-title" style="left:0;width:682px;text-align:center;top:645px">CLIENT TESTIMONIALS</h2>
<div class="abs rule" style="left:397px;top:652px;width:160px;background:#e6e6e6"></div>
<span class="abs" style="left:329px;top:662px;font-family:Georgia,serif;font-size:34px;color:#cfcfcf;font-weight:700">&ldquo;</span>
<svg class="abs" style="left:125px;top:705px" width="10" height="8" viewBox="0 0 10 8"><rect x=".5" y=".5" width="9" height="7" fill="none" stroke="#ccc"/><path d="M7 4H3m1.5-1.5L3 4l1.5 1.5" fill="none" stroke="#999" stroke-width=".6"/></svg>
<p class="abs testimonial">Lorem ipsum dolor sit amet, consectetur adipiscing elit. Mauris imperdiet arcu. Quis pretium nisi mattis vel. Lorem ipsum dolor sit amet, consectetur adipiscing elit. Mauris imperdiet arcu. Quis pretium nisi mattis vel. Lorem ipsum dolor sit amet, consectetur adipiscing elit. Mauris imperdiet arcu. Quis pretium nisi mattis vel.</p>
<svg class="abs" style="left:547px;top:705px" width="10" height="8" viewBox="0 0 10 8"><rect x=".5" y=".5" width="9" height="7" fill="none" stroke="#ccc"/><path d="M3 4h4M5.5 2.5 7 4 5.5 5.5" fill="none" stroke="#999" stroke-width=".6"/></svg>
<p class="abs testimonial-name">JHON DOE</p>

<section class="abs cases"></section>
<div class="abs rule" style="left:125px;top:782px;width:160px;background:#dcdcdc"></div>
<h2 class="abs section-title" style="left:0;width:682px;text-align:center;top:775px">RECENT CASE STUDIES</h2>
<div class="abs rule" style="left:397px;top:782px;width:160px;background:#dcdcdc"></div>
<svg class="abs" style="left:96px;top:824px" width="10" height="18" viewBox="0 0 10 18"><path d="M9 1 1 9l8 8" fill="none" stroke="#666" stroke-width="1.2"/></svg>
<svg class="abs" style="left:576px;top:824px" width="10" height="18" viewBox="0 0 10 18"><path d="m1 1 8 8-8 8" fill="none" stroke="#666" stroke-width="1.2"/></svg>
<figure class="abs case" style="left:125px"><div class="ph" role="img" aria-label="Photo of handcuffs and pills" style="background:linear-gradient(135deg,#7d6f64,#3e3530)"></div><p>Drug Possession</p></figure>
<figure class="abs case" style="left:236px"><div class="ph" role="img" aria-label="Photo of cuffed hands" style="background:linear-gradient(135deg,#6a5a4c,#221c18)"></div><p>Fraud Offenses</p></figure>
<figure class="abs case" style="left:347px"><div class="ph" role="img" aria-label="Photo of a parking ticket on a windshield" style="background:linear-gradient(135deg,#3a3a3a,#a0262a)"></div><p>Traffic Offenses</p></figure>
<figure class="abs case" style="left:458px"><div class="ph" role="img" aria-label="Photo representing domestic violence" style="background:linear-gradient(135deg,#8b7768,#3a2d27)"></div><p>Domestic Violence</p></figure>

<section class="abs contact" aria-label="Contact form"></section>
<h2 class="abs section-title" style="left:0;width:682px;text-align:center;top:911px;color:var(--white)">CONTACT US</h2>
<div class="abs field" style="left:152px;top:943px;width:122px">Name</div>
<div class="abs field" style="left:280px;top:943px;width:122px">Email</div>
<div class="abs field" style="left:409px;top:943px;width:123px">Phone</div>
<div class="abs field" style="left:152px;top:963px;width:380px;height:41px">Brief description of legal issue</div>
<div class="abs agree"><svg class="tick" viewBox="0 0 6 6"><rect width="6" height="6" fill="#fff"/><path d="m1.2 3 1.2 1.2L4.8 1.6" fill="none" stroke="#333" stroke-width=".8"/></svg>I have read and agree to <b>Disclaimer</b></div>
<div class="abs submit">SUBMIT</div>
<svg class="abs" style="left:152px;top:1042px" width="4" height="4"><circle cx="2" cy="2" r="2" fill="#c9b08e"/></svg>
<p class="abs note" style="left:159px">The use of the internet or this form for communication with the firm or any individual member of the firm does not establish an attorney-client relationship. Confidential or time-sensitive information should not be sent through this form.</p>

<footer class="abs footer"></footer>
<h4 class="abs" style="left:125px;top:1092px;font-family:'Roboto Condensed',sans-serif;font-weight:400;color:#fff;font-size:7px">MAIN LINKS</h4>
<div class="abs links" style="left:125px;top:1105px"><div class="on">Home</div><div>Firm Profile</div><div>Attorneys</div><div>Case Results</div></div>
<div class="abs links" style="left:189px;top:1105px"><div>Resources</div><div>Blog</div><div>Contact</div></div>
<h4 class="abs" style="left:270px;top:1092px;font-family:'Roboto Condensed',sans-serif;font-weight:400;color:#fff;font-size:7px">CONTACT US</h4>
<div class="abs" style="left:270px;top:1108px;width:140px">
  <div class="fc-row"><svg class="ic" viewBox="0 0 10 10"><circle cx="5" cy="5" r="4.5" fill="none" stroke="#8d9198" stroke-width=".6"/><path d="M5 2.3a1.8 1.8 0 0 1 1.8 1.8C6.8 5.4 5 7.6 5 7.6S3.2 5.4 3.2 4.1A1.8 1.8 0 0 1 5 2.3Z" fill="#c4c7cc"/></svg><span>1450 Brickell Bay Drive, Suite 900<br>Miami, FL 33131</span></div>
  <div class="fc-row" style="align-items:center"><svg class="ic" viewBox="0 0 10 10"><circle cx="5" cy="5" r="4.5" fill="none" stroke="#8d9198" stroke-width=".6"/><rect x="3.6" y="2.6" width="2.8" height="4.8" rx=".5" fill="#c4c7cc"/></svg><b>305-555-0148</b></div>
  <div class="fc-row" style="align-items:center"><svg class="ic" viewBox="0 0 10 10"><circle cx="5" cy="5" r="4.5" fill="none" stroke="#8d9198" stroke-width=".6"/><rect x="2.8" y="3.4" width="4.4" height="3.4" fill="#c4c7cc"/><rect x="3.5" y="2.4" width="3" height="1.2" fill="#c4c7cc"/></svg><b>305-555-0149</b></div>
  <div class="fc-row" style="align-items:center"><svg class="ic" viewBox="0 0 10 10"><circle cx="5" cy="5" r="4.5" fill="none" stroke="#8d9198" stroke-width=".6"/><rect x="2.8" y="3.3" width="4.4" height="3.2" fill="#c4c7cc"/></svg><span style="color:#3e6ea8">hello@benavideslaw.net</span></div>
</div>
<div class="abs fbrand">Loreta Benavides-Kurtz<small>ATTORNEY AT LAW</small></div>
<div class="abs social" aria-label="Social profiles"><i></i><i></i><i></i><i></i><i></i><i></i></div>
<p class="abs copy">&copy;2016 <b>Loreta Benavides-Kurtz.</b> All rights reserved.</p>

</body>
</html>
```